Velkora - 13 different skin care oil bottle label designs

We need label designs for our private label Velkora.
The labels should be designed in Adobe Illustator. Please use warm or lightening colours. We like colours. But they should have a uniform look. It is necessary to show the fruit/trees/nuts. On the back label we will have description text in four languages, a barcode, Made in France, an adress.
We will use oval clear/transparent bottles. The label size for 150 ml is 50 x 90 mm. Label size for 250 ml bottles is 60 x 115 mm.
Argan Oil 150 ml 100% PURE
Avocado Oil 150 ml 100% PURE
Castor Oil 150 ml 100% PURE
Jojoba's Oil 150 ml 100% PURE
Apricot Oil 150 ml 100% PURE
Coconut Oil 150 ml 100% PURE
Macadamia's Oil 150 ml 100% PURE
Neem Oil 150 ml 100% PURE
Almond Oil 150 ml 100% PURE
Wheat germ Oil 150 ml 100% PURE
Pure Glycerine 250 ml
Pure Glycerine + rose water 250 ml
Parafin Oil 250 ml

```html
<!DOCTYPE html>
<html lang="en">
<head>
<meta charset="utf-8">
<title>Velkora – Oil Bottle Labels</title>
<link href="https://fonts.googleapis.com/css2?family=Questrial&display=swap" rel="stylesheet">
<style>
  :root {
    --stage-top: #ebeaea;
    --stage-bottom: #ffffff;
    --brand-green: #a3cc3a;
    --brand-green-light: #c9e27f;
    --brand-green-soft: #b5d45a;
    --pure-grey: #9a9a9a;
    --ink: #3a2a1a;
    --white: #ffffff;
    --argan-dark: #8a4a1f;
    --argan-mid: #a8693a;
    --argan-light: #d2ab88;
    --argan-pale: #ecdccc;
    --apricot-deep: #f5c21a;
    --apricot-mid: #f8d65a;
    --apricot-light: #fbe59a;
    --apricot-pale: #fdf1c8;
  }
  * { margin: 0; padding: 0; box-sizing: border-box; }
  html, body { width: 1200px; height: 900px; overflow: hidden; }
  body {
    font-family: "Questrial", "Helvetica Neue", Arial, sans-serif;
    background: linear-gradient(to bottom, var(--stage-top) 0%, #f6f6f6 55%, var(--stage-bottom) 88%);
    position: relative;
  }
  .label {
    position: absolute;
    top: 138px;
    width: 337px;
    height: 608px;
    overflow: hidden;
  }
  .label--argan {
    left: 183px;
    background: linear-gradient(to bottom, var(--white) 0%, var(--white) 55%, var(--argan-pale) 66%, var(--argan-light) 78%, var(--argan-mid) 90%, var(--argan-dark) 100%);
  }
  .label--apricot {
    left: 587px;
    background: linear-gradient(to bottom, var(--white) 0%, var(--white) 55%, var(--apricot-pale) 68%, var(--apricot-light) 80%, var(--apricot-mid) 90%, var(--apricot-deep) 100%);
  }
  .label__swoosh { position: absolute; left: 0; top: 0; width: 337px; height: 608px; }
  .brand {
    position: absolute;
    left: 130px;
    top: 70px;
    width: 170px;
    text-align: center;
  }
  .brand__dot {
    display: block;
    width: 84px;
    height: 84px;
    margin: 0 auto;
    border-radius: 50%;
    background: var(--brand-green-soft);
  }
  .brand__name {
    display: block;
    margin-top: 8px;
    font-size: 36px;
    line-height: 1;
    color: var(--brand-green-light);
    letter-spacing: 0.5px;
  }
  .name-band {
    position: absolute;
    left: 0;
    top: 235px;
    width: 100%;
    height: 55px;
    background: var(--brand-green);
    box-shadow: 0 6px 0 var(--brand-green-light);
  }
  .name-band__title {
    position: absolute;
    left: 20px;
    top: 11px;
    font-size: 29px;
    font-weight: 400;
    color: var(--white);
  }
  .purity {
    position: absolute;
    right: 24px;
    top: 313px;
    font-size: 19px;
    color: var(--pure-grey);
    letter-spacing: 0.3px;
  }
  .volume {
    position: absolute;
    right: 26px;
    top: 574px;
    font-size: 11px;
    color: var(--ink);
  }
  .product-visual { position: absolute; }
  .product-visual--argan {
    left: 24px; top: 340px; width: 210px; height: 205px;
    border-radius: 50% 55% 45% 50%;
    background: radial-gradient(ellipse at 55% 55%, #b0703a 0%, #8f5328 50%, rgba(143,83,40,0) 72%);
  }
  .product-visual--apricot {
    left: 58px; top: 420px; width: 170px; height: 135px;
    border-radius: 50%;
    background: radial-gradient(ellipse at 55% 50%, #f7a85a 0%, #f08a3a 45%, rgba(240,138,58,0) 72%);
  }
</style>
</head>
<body>

  <section class="label label--argan" aria-label="Argan Oil label">
    <svg class="label__swoosh" viewBox="0 0 337 608" aria-hidden="true">
      <path d="M0 0 H165 C85 70 62 230 108 360 C70 300 30 280 0 270 Z" fill="#c49a74"/>
      <path d="M0 0 H118 C64 80 58 240 100 352 C62 290 24 265 0 250 Z" fill="#ab7446"/>
      <path d="M0 0 H70 C40 90 52 250 95 345 C55 285 20 250 0 230 Z" fill="#99602f"/>
      <path d="M60 0 C30 120 55 260 102 358" stroke="#d8b894" stroke-width="2" fill="none" opacity="0.7"/>
      <path d="M100 0 C56 110 62 270 106 362" stroke="#e6cdb3" stroke-width="1.5" fill="none" opacity="0.6"/>
    </svg>
    <div class="product-visual product-visual--argan" role="img" aria-label="Photo of argan nuts, one cracked open"></div>
    <div class="brand"><span class="brand__dot"></span><span class="brand__name">Velkora</span></div>
    <div class="name-band"><h2 class="name-band__title">Argan Oil</h2></div>
    <p class="purity">100% PURE</p>
    <p class="volume">150 ml</p>
  </section>

  <section class="label label--apricot" aria-label="Apricot Oil label">
    <svg class="label__swoosh" viewBox="0 0 337 608" aria-hidden="true">
      <path d="M0 0 H165 C85 70 62 230 108 360 C70 300 30 280 0 270 Z" fill="#fdeaa6"/>
      <path d="M0 0 H118 C64 80 58 240 100 352 C62 290 24 265 0 250 Z" fill="#fbdc72"/>
      <path d="M0 0 H70 C40 90 52 250 95 345 C55 285 20 250 0 230 Z" fill="#f8cd3c"/>
      <path d="M60 0 C30 120 55 260 102 358" stroke="#fff3c8" stroke-width="2" fill="none" opacity="0.8"/>
      <path d="M100 0 C56 110 62 270 106 362" stroke="#fff6d8" stroke-width="1.5" fill="none" opacity="0.7"/>
    </svg>
    <div class="product-visual product-visual--apricot" role="img" aria-label="Photo of a whole apricot and a halved apricot with its stone and a leaf"></div>
    <div class="brand"><span class="brand__dot"></span><span class="brand__name">Velkora</span></div>
    <div class="name-band"><h2 class="name-band__title">Apricot Oil</h2></div>
    <p class="purity">100% PURE</p>
    <p class="volume">150 ml</p>
  </section>

</body>
</html>
```